We specialize in pizza, pasta and salads and are now offering TAKE & BAKE and GRAB & GO ...

Looking for either a 8.5" x 11" or similar for a instore display. WILL BE ON A SWIVELING HOLDER to catch customers attention.

**THIS IS A DOUBLE SIDED PRINT**

ONE SIDE will consist of WHAT'S FOR DINNER TONIGHT? and the following:
* Take & Bake"
* "Baked Pasta"
* Freshly made in house
* Lasagna
$13.50
- please include attached closeup picture and logo

THE OTHER SIDE will consist of
mini charcutier board.
* snack size charcutier delight *
* Enjoy the flavors of gourmet snacking, all in one convenient box!

PRICE $8.99

Winning design will be commissioned to design labels for "grab and go" for take and bake pasta, charcuterie box, pasta salads, candy etc.

Thank you and please do not hesitate to ask any questions.

www.calderipizza.ca
www.fernloop.ca
Logo to be interchanged as they are affiliated meaning FernLoop is a brand within Calderi pizza.

Target Market(s)

our target market is customers who have already entered our business. This is to upsel

Industry/Entity Type

We are in a self serve enviroment and target business people

Requirements
Must have
• must be clean and catchy. We are located in a professional business community.
Nice to have
• Must be appealing, appetizing and utilize our website colors
Should not have
• should not have any carton drawings and not be cluttered (busy)

```html
<!DOCTYPE html>
<html lang="en">
<head>
<meta charset="utf-8">
<title>Calderi Pizza – In-store Display Cards</title>
<link href="https://fonts.googleapis.com/css2?family=Jost:wght@400;700&display=swap" rel="stylesheet">
<style>
  :root {
    --stage: #8a8a8a;
    --ink: #000000;
    --brand-red: #a93226;
    --badge-red: #c8161d;
    --badge-dark: #8e0d12;
    --paper: #ffffff;
    --wood: #4a3a32;
  }
  html, body {
    margin: 0;
    padding: 0;
    width: 1200px;
    height: 1200px;
    overflow: hidden;
    background: var(--stage);
    font-family: "Jost", sans-serif;
  }
  .display-set {
    position: relative;
    width: 1200px;
    height: 1200px;
  }
  .card {
    position: absolute;
    top: 316px;
    width: 440px;
    height: 568px;
    background: var(--brand-red);
    overflow: hidden;
    box-shadow: 4px 5px 6px rgba(0,0,0,0.35);
  }
  .card--dinner { left: 136px; }
  .card--charcuterie { left: 624px; }

  .card__top {
    position: absolute;
    left: 0; top: 0;
    width: 100%;
    height: 253px;
    background: var(--ink);
    border-bottom: 3px solid var(--paper);
  }
  .brand-plate {
    position: absolute;
    left: 101px; top: 0;
    width: 237px; height: 59px;
    background: var(--paper);
    display: flex;
    align-items: center;
    justify-content: center;
    gap: 8px;
  }
  .brand-plate__dot {
    width: 14px; height: 14px;
    border-radius: 50%;
    background: var(--brand-red);
  }
  .brand-plate__name {
    font-size: 25px;
    font-weight: 400;
    letter-spacing: 1px;
    color: var(--brand-red);
    text-transform: uppercase;
  }
  .headline {
    position: absolute;
    left: 0; width: 100%;
    margin: 0;
    text-align: center;
    color: var(--paper);
    font-weight: 400;
    font-size: 24px;
    line-height: 1;
  }
  .card--dinner .headline { top: 82px; font-size: 23px; }
  .card--charcuterie .headline { top: 96px; }
  .headline strong { font-weight: 700; }

  .bracket {
    position: absolute;
    width: 72px; height: 70px;
  }
  .bracket--top-left {
    border-top: 9px solid var(--paper);
    border-left: 9px solid var(--paper);
    box-sizing: border-box;
  }
  .bracket--bottom-right {
    border-bottom: 9px solid var(--paper);
    border-right: 9px solid var(--paper);
    box-sizing: border-box;
  }

  .photo {
    position: absolute;
    border: 3px solid var(--paper);
    box-sizing: border-box;
  }
  .photo--pasta-pan {
    left: 36px; top: 147px; width: 268px; height: 249px;
    background: radial-gradient(ellipse at 50% 55%, #d9b36a 0%, #b98a45 28%, #3a3330 48%, #5a4638 70%, #3b2f2a 100%);
  }
  .photo--lasagna {
    left: 255px; top: 320px; width: 144px; height: 136px;
    background: radial-gradient(ellipse at 50% 60%, #e9a94e 0%, #d98a3a 40%, #f4efe6 70%, #c9b9a3 100%);
  }
  .photo--board {
    left: 40px; top: 176px; width: 357px; height: 248px;
    background: radial-gradient(ellipse at 55% 65%, #e59a9a 0%, #c97070 28%, #5b4a40 60%, #2f2824 100%);
  }

  .price-badge {
    position: absolute;
    width: 100px; height: 100px;
    left: 317px; top: 133px;
  }
  .card--charcuterie .price-badge { left: 318px; }
  .price-badge__text {
    position: absolute;
    left: 0; top: 22px;
    width: 100%;
    text-align: center;
    color: var(--paper);
    line-height: 1.05;
  }
  .price-badge__label { display: block; font-weight: 700; font-size: 18px; letter-spacing: 0.5px; }
  .price-badge__amount { display: block; font-weight: 400; font-size: 17px; }

  .features {
    position: absolute;
    left: 36px;
    margin: 0;
    padding: 0 0 0 18px;
    color: var(--paper);
    font-size: 20px;
    line-height: 28px;
  }
  .card--dinner .features { top: 414px; }
  .card--charcuterie .features { top: 455px; width: 370px; line-height: 27px; }
  .features li { padding-left: 2px; }
</style>
</head>
<body>
<main class="display-set">

  <!-- Side A: Dinner -->
  <section class="card card--dinner">
    <div class="card__top"></div>
    <div class="brand-plate"><span class="brand-plate__dot"></span><span class="brand-plate__name">Calderi Pizza</span></div>
    <h1 class="headline">WHAT'S FOR DINNER <strong>TONIGHT?</strong></h1>
    <div class="bracket bracket--top-left" style="left:11px; top:121px;"></div>
    <div class="photo photo--pasta-pan" role="img" aria-label="Pan of bow-tie pasta with ground meat and herbs on a wooden board"></div>
    <div class="bracket bracket--bottom-right" style="left:352px; top:410px;"></div>
    <div class="photo photo--lasagna" role="img" aria-label="Plated slice of baked lasagna with basil"></div>
    <div class="price-badge">
      <svg width="100" height="100" viewBox="0 0 100 100" aria-hidden="true">
        <defs>
          <radialGradient id="badgeFillA" cx="45%" cy="35%" r="65%">
            <stop offset="0" stop-color="#e0262c"/>
            <stop offset="1" stop-color="#8e0d12"/>
          </radialGradient>
        </defs>
        <circle cx="50" cy="50" r="45" fill="none" stroke="#a8141a" stroke-width="8" stroke-dasharray="3 2.3"/>
        <circle cx="50" cy="50" r="44" fill="url(#badgeFillA)"/>
        <path d="M70 88 L92 64 L86 86 Z" fill="#d9d9d9"/>
        <path d="M70 88 L92 64" stroke="#ffffff" stroke-width="2"/>
      </svg>
      <div class="price-badge__text"><span class="price-badge__label">PRICE</span><span class="price-badge__amount">$13.50</span></div>
    </div>
    <ul class="features">
      <li>Take &amp; Bake</li>
      <li>Baked Pasta</li>
      <li>Freshly made in house</li>
      <li>Lasagna</li>
    </ul>
  </section>

  <!-- Side B: Charcuterie -->
  <section class="card card--charcuterie">
    <div class="card__top"></div>
    <div class="brand-plate"><span class="brand-plate__dot"></span><span class="brand-plate__name">Calderi Pizza</span></div>
    <h1 class="headline">Mini <strong>charcutier</strong> board.</h1>
    <div class="bracket bracket--top-left" style="left:11px; top:148px;"></div>
    <div class="photo photo--board" role="img" aria-label="Sliced cured meats with lettuce, dip and flatbread on a wooden table"></div>
    <div class="bracket bracket--bottom-right" style="left:355px; top:383px;"></div>
    <div class="price-badge">
      <svg width="100" height="100" viewBox="0 0 100 100" aria-hidden="true">
        <defs>
          <radialGradient id="badgeFillB" cx="45%" cy="35%" r="65%">
            <stop offset="0" stop-color="#e0262c"/>
            <stop offset="1" stop-color="#8e0d12"/>
          </radialGradient>
        </defs>
        <circle cx="50" cy="50" r="45" fill="none" stroke="#a8141a" stroke-width="8" stroke-dasharray="3 2.3"/>
        <circle cx="50" cy="50" r="44" fill="url(#badgeFillB)"/>
        <path d="M70 88 L92 64 L86 86 Z" fill="#d9d9d9"/>
        <path d="M70 88 L92 64" stroke="#ffffff" stroke-width="2"/>
      </svg>
      <div class="price-badge__text"><span class="price-badge__label">PRICE</span><span class="price-badge__amount">$8.99</span></div>
    </div>
    <ul class="features">
      <li>Snack size charcutier delight</li>
      <li>Enjoy the flavors of gourmet snacking, all in one convenient box!</li>
    </ul>
  </section>

</main>
</body>
</html>
```